依頼詳細
会社の名刺のデザインをやり直したいと思っています。
記載項目
会社名、肩書き、氏名、電話番号、FAX、メルアド
希望イメージ
シンプル 複雑
単色 カラフル
暗い 明るい
日常 高級
遊び心 厳粛
未来的 伝統的
女性的 男性的
希望する色
赤系、緑系、水色系
納品ファイル
• 高解像度JPG (.jpg)
• イラストレーター形式 (.ai)
• フォトショップ形式 (.psd)
• PNG形式 (.png)

```html
<!DOCTYPE html>
<html lang="ja">
<head>
<meta charset="utf-8">
<title>名刺デザイン ミルネ菓子舎</title>
<link href="https://fonts.googleapis.com/css2?family=M+PLUS+Rounded+1c:wght@400;700;800&display=swap" rel="stylesheet">
<style>
  :root {
    --page-bg: #f3f3f3;
    --card-white: #ffffff;
    --brand-pink: #e8737a;
    --back-pink: #e9747b;
    --text-dark: #3a3a3a;
    --text-mid: #555555;
    --sweet-mint: rgba(120, 200, 185, 0.55);
    --sweet-yellow: rgba(235, 205, 110, 0.5);
    --sweet-blue: rgba(120, 190, 225, 0.5);
    --sweet-pink: rgba(235, 130, 150, 0.5);
    --back-light: rgba(255, 225, 170, 0.28);
    --back-cream: rgba(255, 245, 230, 0.22);
  }
  * { margin: 0; padding: 0; box-sizing: border-box; }
  html, body {
    width: 900px; height: 1200px; overflow: hidden;
    background: var(--page-bg);
    font-family: "M PLUS Rounded 1c", sans-serif;
  }
  .card {
    position: absolute; left: 57px; width: 786px; height: 470px;
    box-shadow: 0 3px 10px rgba(0,0,0,0.12);
    overflow: hidden;
  }
  .card-front { top: 45px; background: var(--card-white); }
  .card-back { top: 640px; background: var(--back-pink); }

  .sweets-art { position: absolute; }
  .sweets-top-left {
    left: 0; top: 0; width: 360px; height: 170px;
    background:
      radial-gradient(closest-side at 18% 50%, var(--sweet-yellow), transparent),
      radial-gradient(closest-side at 45% 45%, var(--sweet-pink), transparent),
      radial-gradient(closest-side at 78% 40%, var(--sweet-mint), transparent);
  }
  .sweets-right {
    left: 420px; top: 40px; width: 366px; height: 430px;
    background:
      radial-gradient(closest-side at 80% 22%, var(--sweet-yellow), transparent),
      radial-gradient(closest-side at 30% 58%, var(--sweet-mint), transparent),
      radial-gradient(closest-side at 75% 55%, var(--sweet-pink), transparent),
      radial-gradient(closest-side at 40% 88%, var(--sweet-blue), transparent),
      radial-gradient(closest-side at 82% 85%, var(--sweet-pink), transparent);
  }
  .sweets-pattern {
    inset: 0;
    background:
      radial-gradient(closest-side at 15% 20%, var(--back-light), transparent),
      radial-gradient(closest-side at 50% 15%, var(--back-cream), transparent),
      radial-gradient(closest-side at 85% 25%, var(--back-light), transparent),
      radial-gradient(closest-side at 12% 75%, var(--back-cream), transparent),
      radial-gradient(closest-side at 50% 85%, var(--back-light), transparent),
      radial-gradient(closest-side at 88% 78%, var(--back-cream), transparent);
  }

  .brand-name {
    position: absolute;
    font-weight: 800; letter-spacing: 1px; white-space: nowrap; line-height: 1;
  }
  .card-front .brand-name {
    left: 500px; top: 30px; font-size: 34px; color: var(--brand-pink);
  }
  .card-back .brand-name {
    left: 190px; top: 225px; font-size: 46px; color: var(--card-white);
  }

  .holder { position: absolute; left: 48px; top: 238px; color: var(--text-dark); }
  .holder-name { font-size: 30px; font-weight: 700; letter-spacing: 3px; line-height: 1.2; }
  .holder-name .romaji { font-size: 15px; font-weight: 400; letter-spacing: 1px; margin-left: 12px; color: var(--text-mid); }
  .holder-title { font-size: 13px; margin-top: 6px; letter-spacing: 2px; }

  .contact { position: absolute; left: 48px; top: 330px; color: var(--text-dark); font-size: 13px; line-height: 22px; }
  .contact .company { font-size: 14px; letter-spacing: 1px; }
</style>
</head>
<body>
  <section class="card card-front">
    <div class="sweets-art sweets-top-left" role="img" aria-label="マカロンやキャンディなど線画のお菓子イラスト"></div>
    <div class="sweets-art sweets-right" role="img" aria-label="ケーキ、ソフトクリーム、ドーナツ、チョコレート、クッキーの線画イラスト"></div>
    <div class="brand-name">ミルネ菓子舎</div>
    <div class="holder">
      <p class="holder-name">苗字名前<span class="romaji">NAMAE MYOJI</span></p>
      <p class="holder-title">代表取締役</p>
    </div>
    <div class="contact">
      <p class="company">株式会社〇〇〇〇</p>
      <p>〒000-0000東京都〇〇区〇〇0-0-0</p>
      <p>〇〇〇〇ビル6F</p>
      <p>TEL 000-0000-0000　FAX 00-0000-0000</p>
      <p>MAIL aaaaaaaa@aaaaaaa.aa</p>
    </div>
  </section>

  <section class="card card-back">
    <div class="sweets-art sweets-pattern" role="img" aria-label="ドーナツ、カップケーキ、クロワッサン、キャンディ、チョコレートなどのお菓子線画パターン"></div>
    <div class="brand-name">ミルネ菓子舎</div>
  </section>
</body>
</html>
```